Maple Thistlewood - New monument signage for our apartment community

We have a monument sign that we would like to replace with a fresh, clean, and easy to read new design. I've included a couple pictures of the physical sign - people will be seeing this while driving very fast. It needs to be simple and easy to quickly see while driving.

* Maple Thistlewood
* Newly Renovated!
* www.maplethistlewoodhomes.example
* 555 - 318 - 7906

Suggestions:
* Bright colors
* Bold fonts
* Focus on phone number being easy to read

*** I attached a picture of something similar we did at one of our other apartment communities (Ferncliff townhomes)

Maple Thistlewood Apartment Community

```html
<!DOCTYPE html>
<html lang="en">
<head>
<meta charset="utf-8">
<title>Maple Thistlewood Apartment Community – Monument Sign</title>
<link rel="stylesheet" href="https://fonts.googleapis.com/css2?family=Abril+Fatface&family=Josefin+Sans:wght@400;600;700&display=swap">
<style>
  :root {
    --sign-blue: #2e88c8;
    --sign-green: #2d8634;
    --sign-white: #ffffff;
    --wave-shadow: rgba(0, 0, 0, 0.28);
  }
  html, body {
    margin: 0;
    padding: 0;
    width: 1200px;
    height: 665px;
    overflow: hidden;
    background: var(--sign-white);
  }
  .monument-sign {
    position: relative;
    width: 1200px;
    height: 665px;
    background: var(--sign-white);
  }
  .sign-art {
    position: absolute;
    inset: 0;
    width: 1200px;
    height: 665px;
    display: block;
  }
  .wave { fill: var(--sign-blue); }
  .tagline {
    font-family: "Josefin Sans", sans-serif;
    font-weight: 700;
    font-size: 50px;
    fill: var(--sign-green);
    letter-spacing: 1px;
  }
  .community-name {
    font-family: "Abril Fatface", serif;
    font-size: 156px;
    fill: var(--sign-blue);
  }
  .community-type {
    font-family: "Josefin Sans", sans-serif;
    font-weight: 400;
    font-size: 64px;
    fill: var(--sign-blue);
  }
  .phone-number {
    font-family: "Abril Fatface", serif;
    font-size: 196px;
    fill: var(--sign-green);
  }
  .footer-band { fill: var(--sign-blue); }
  .website {
    font-family: "Josefin Sans", sans-serif;
    font-weight: 600;
    font-size: 50px;
    fill: var(--sign-white);
  }
</style>
</head>
<body>
<main class="monument-sign">
  <svg class="sign-art" viewBox="0 0 1200 665" xmlns="http://www.w3.org/2000/svg">
    <defs>
      <filter id="wave-lift" x="-5%" y="-20%" width="110%" height="160%">
        <feDropShadow dx="0" dy="5" stdDeviation="4" flood-color="#000" flood-opacity="0.28"/>
      </filter>
    </defs>

    <g class="header-waves" filter="url(#wave-lift)">
      <path class="wave wave-thin"
            d="M0 40 C150 -4, 400 8, 600 68 C800 128, 1000 150, 1200 66 L1200 86 C1000 168, 800 146, 600 88 C400 28, 150 14, 0 58 Z"/>
      <path class="wave wave-broad"
            d="M380 0 L1200 0 L1200 22 C1050 92, 850 100, 680 62 C560 34, 460 10, 380 0 Z"/>
    </g>

    <g class="tagline-block" text-anchor="middle">
      <text class="tagline" x="216" y="72">NEWLY</text>
      <text class="tagline" x="216" y="124">RENOVATED!</text>
    </g>

    <text class="community-name" x="59" y="291" textLength="1081" lengthAdjust="spacingAndGlyphs">Maple Thistlewood</text>
    <text class="community-type" x="124" y="367" textLength="952" lengthAdjust="spacing">APARTMENT COMMUNITY</text>

    <text class="phone-number" x="59" y="564" textLength="1081" lengthAdjust="spacingAndGlyphs">555 - 318 - 7906</text>

    <rect class="footer-band" x="0" y="605" width="1200" height="60"/>
    <text class="website" x="600" y="651" text-anchor="middle" textLength="945" lengthAdjust="spacingAndGlyphs">www.maplethistlewoodhomes.example</text>
  </svg>
</main>
</body>
</html>
```